Indie musician needs album cover art

I am an independant musician releasing my second album via digital sources. I plan to make it available on Vendly and other digital stores but primarily distribute it free through Tunegrove.

The album's music style is a blend of singer-songwriter folk, punk, alt country, electronic rock and spoken word. The lyrical content is a dark journey through travel in foreign countries, relationships, airports and theatres, formed during my own journey as an audio engineer for a travelling theatre show.

The album is called "Ash Under Glass" - at times both a plea and a directive. I would like the album cover to reflect a sense of longing, restlessness, unease and movement. A subversive tone is also possible.

I have had a go at designing a couple of ideas myself, using my own photos. I like the ideas but I am not skilled in graphic design and am unable to take them further to get the right feel and look. I will post these as examples of tone. The finished work does not need to copy either of these.

A .zip of the album can be downloaded here (low fi mp3):

http://fylo.io/Qx7rT4

Target Market(s)

People who enjoy thoughtful, honest, homemade music. Definitely not a teeny pop audience. Adult, subversive, educated, emotional...

Industry/Entity Type

Graphic Design

Requirements
Must have
• Artist name (no caps): kipwren
Album name (prefer no caps): ash under glass

```html
<!DOCTYPE html>
<html lang="en">
<head>
<meta charset="utf-8">
<title>kipwren — ash under glass</title>
<link rel="stylesheet" href="https://fonts.googleapis.com/css2?family=Poiret+One&display=swap">
<style>
  :root {
    --backdrop: #ffffff;
    --sky: #1f3f9c;
    --dusk: #3b63c9;
    --street-glow: #f2b98f;
    --crowd-red: #d9583f;
    --crowd-amber: #f0a35e;
    --pavement: #f4d2b8;
    --pavement-light: #f7e0cf;
    --band: rgba(92, 80, 72, 0.6);
    --band-text: #f6efe9;
    --title-text: #2b241f;
  }
  * { margin: 0; padding: 0; box-sizing: border-box; }
  html, body {
    width: 1200px;
    height: 848px;
    overflow: hidden;
    background: var(--backdrop);
  }
  .canvas {
    position: relative;
    width: 1200px;
    height: 848px;
  }
  .album-cover {
    position: absolute;
    left: 325px;
    top: 96px;
    width: 548px;
    height: 547px;
    overflow: hidden;
  }
  .cover-photo {
    position: absolute;
    inset: 0;
    background: linear-gradient(180deg,
      var(--sky) 0%,
      var(--dusk) 14%,
      #a94a3e 24%,
      #e8875a 34%,
      var(--street-glow) 48%,
      var(--pavement) 72%,
      var(--pavement-light) 100%);
  }
  .motion-streaks {
    position: absolute;
    inset: 0;
    filter: blur(10px);
    background:
      radial-gradient(ellipse 38% 5% at 22% 58%, rgba(217, 88, 63, 0.75), transparent 100%),
      radial-gradient(ellipse 30% 4% at 30% 66%, rgba(200, 70, 50, 0.6), transparent 100%),
      radial-gradient(ellipse 34% 4% at 18% 74%, rgba(217, 88, 63, 0.55), transparent 100%),
      radial-gradient(ellipse 42% 5% at 55% 50%, rgba(240, 163, 94, 0.7), transparent 100%),
      radial-gradient(ellipse 36% 3.5% at 60% 60%, rgba(236, 140, 90, 0.5), transparent 100%),
      radial-gradient(ellipse 40% 4% at 70% 44%, rgba(230, 200, 110, 0.5), transparent 100%),
      radial-gradient(ellipse 46% 4% at 45% 40%, rgba(230, 110, 70, 0.55), transparent 100%),
      radial-gradient(ellipse 50% 3% at 50% 82%, rgba(235, 170, 140, 0.45), transparent 100%),
      repeating-linear-gradient(180deg,
        rgba(255, 255, 255, 0) 0px,
        rgba(255, 230, 210, 0.18) 6px,
        rgba(220, 110, 80, 0.1) 12px,
        rgba(255, 255, 255, 0) 18px);
  }
  .artist-band {
    position: absolute;
    left: 0;
    top: 464px;
    width: 194px;
    height: 53px;
    background: var(--band);
    display: flex;
    align-items: center;
    padding-left: 42px;
  }
  .artist-name {
    font-family: "Poiret One", sans-serif;
    font-weight: 400;
    font-size: 31px;
    color: var(--band-text);
    letter-spacing: 0.5px;
  }
  .album-title {
    position: absolute;
    right: 38px;
    top: 472px;
    font-family: "Poiret One", sans-serif;
    font-weight: 400;
    font-size: 31px;
    line-height: 1.2;
    color: var(--title-text);
    letter-spacing: 0.6px;
  }
</style>
</head>
<body>
  <main class="canvas">
    <section class="album-cover">
      <div class="cover-photo" role="img" aria-label="Long-exposure night photograph of a busy resort street, crowds blurred into orange and red streaks beneath shop lights and a deep blue sky">
        <div class="motion-streaks"></div>
      </div>
      <div class="artist-band"><span class="artist-name">kipwren</span></div>
      <h1 class="album-title">ash under glass</h1>
    </section>
  </main>
</body>
</html>
```